Eye catching business card

2 sided
Black background with logo in color on one side along with the words "Proudly serving the commercial and defense industries since 1975"
2nd side to contain contact information (see attached current business card) and "Waterjet, Composite, Precision Machining and Clean Room Manufacturing" with a very faint watermark of a waving USA Flag in the back ground.
Remove the "est. 195" from the current logo design

```html
<!DOCTYPE html>
<html lang="en">
<head>
<meta charset="UTF-8">
<title>Northfield Machine Works – Business Card</title>
<link href="https://fonts.googleapis.com/css2?family=Montserrat:wght@300;400;500;600;700&display=swap" rel="stylesheet">
<style>
  :root {
    --bg: #161616;
    --card: #252526;
    --card-edge: #2e2e2f;
    --silver: #a9aaac;
    --text: #e9e9ea;
    --muted: #8a8b8d;
    --blue: #2f9be4;
    --blue-deep: #2f6fd1;
    --rule: #5a5b5d;
  }
  * { box-sizing: border-box; margin: 0; padding: 0; }
  html, body { width: 1200px; height: 1200px; overflow: hidden; }
  body {
    background: var(--bg);
    font-family: "Montserrat", sans-serif;
    color: var(--text);
    position: relative;
  }
  .card {
    position: absolute;
    left: 160px;
    width: 880px;
    height: 503px;
    background: linear-gradient(160deg, var(--card-edge), var(--card));
    border-radius: 26px;
    overflow: hidden;
    box-shadow: 0 14px 40px rgba(0,0,0,.6);
  }
  .card--front { top: 70px; }
  .card--back { top: 627px; }

  .brand {
    display: flex;
    align-items: center;
    gap: 14px;
    font-weight: 700;
    color: var(--silver);
    letter-spacing: 1px;
    text-transform: uppercase;
    white-space: nowrap;
  }
  .brand__mark {
    width: 26px; height: 26px;
    background: var(--blue);
    flex: none;
  }

  /* front */
  .card--front .brand {
    position: absolute;
    top: 190px; left: 0; right: 0;
    justify-content: center;
    font-size: 42px;
  }
  .tagline {
    position: absolute;
    left: 40px; right: 40px; bottom: 60px;
    text-align: center;
    font-size: 17px;
    font-weight: 500;
    letter-spacing: 1.6px;
    color: var(--muted);
    white-space: nowrap;
  }
  .tagline__accent { color: var(--blue); font-weight: 600; }

  /* back */
  .card--back .brand {
    position: absolute;
    top: 60px; left: 70px;
    font-size: 34px;
  }
  .person {
    position: absolute;
    top: 160px; left: 70px;
    display: flex; align-items: baseline; gap: 18px;
  }
  .person__name { font-size: 30px; font-weight: 300; letter-spacing: .5px; }
  .person__name b { font-weight: 700; }
  .person__title { font-size: 20px; font-weight: 700; color: var(--blue); letter-spacing: 1px; }
  .rule {
    position: absolute;
    top: 212px; left: 70px; right: 90px;
    height: 1px; background: var(--rule);
  }
  .contacts {
    position: absolute;
    top: 232px; left: 70px;
    list-style: none;
    font-size: 21px;
    line-height: 34px;
  }
  .contacts li { display: flex; align-items: center; gap: 14px; }
  .contacts svg { width: 18px; height: 18px; fill: var(--blue); flex: none; }
  .address {
    position: absolute;
    right: 90px; top: 300px;
    text-align: right;
    font-size: 21px;
    line-height: 30px;
    font-style: normal;
  }
  .band {
    position: absolute;
    left: 0; right: 0; bottom: 0;
    height: 66px;
    padding: 0 40px;
    background: linear-gradient(90deg, var(--blue-deep), var(--blue), var(--blue-deep));
    display: flex; align-items: center; justify-content: center;
    font-size: 19px; font-weight: 600; letter-spacing: 1px;
    color: #fff;
    white-space: nowrap;
  }
</style>
</head>
<body>

<section class="card card--front">
  <div class="brand"><span class="brand__mark"></span>Northfield Machine Works</div>
  <p class="tagline">PROUDLY SERVING THE COMMERCIAL AND DEFENSE INDUSTRIES <span class="tagline__accent">SINCE 1975</span></p>
</section>

<section class="card card--back">
  <div class="brand"><span class="brand__mark"></span>Northfield Machine Works</div>
  <div class="person">
    <span class="person__name"><b>DALE</b> PORTER</span>
    <span class="person__title">PRESIDENT</span>
  </div>
  <div class="rule"></div>
  <ul class="contacts">
    <li><svg viewBox="0 0 24 24"><path d="M6.6 10.8a15 15 0 0 0 6.6 6.6l2.2-2.2c.3-.3.7-.4 1-.2 1.1.4 2.3.6 3.6.6.6 0 1 .4 1 1V20c0 .6-.4 1-1 1A17 17 0 0 1 3 4c0-.6.4-1 1-1h3.5c.6 0 1 .4 1 1 0 1.3.2 2.5.6 3.6.1.3 0 .7-.2 1z"/></svg>555-014-0108 (Office)</li>
    <li><svg viewBox="0 0 24 24"><path d="M6 3h12v5H6zM4 9h16a2 2 0 0 1 2 2v6h-4v4H6v-4H2v-6a2 2 0 0 1 2-2zm4 7v3h8v-3z"/></svg>555-014-0140</li>
    <li><svg viewBox="0 0 24 24"><path d="M2 5h20v14H2zm2 2v.5l8 5 8-5V7z"/></svg>dale@northfieldmw.com</li>
    <li><svg viewBox="0 0 24 24"><path d="M12 2a10 10 0 1 0 0 20 10 10 0 0 0 0-20zm6.9 6h-3a15 15 0 0 0-1.3-3.9A8 8 0 0 1 18.9 8zM12 4c.8 1.2 1.5 2.5 1.9 4h-3.8c.4-1.5 1.1-2.8 1.9-4zM4.3 14a8 8 0 0 1 0-4h3.4a16 16 0 0 0 0 4zm.8 2h3a15 15 0 0 0 1.3 3.9A8 8 0 0 1 5.1 16zm3-8h-3a8 8 0 0 1 4.3-3.9A15 15 0 0 0 8.1 8zM12 20c-.8-1.2-1.5-2.5-1.9-4h3.8c-.4 1.5-1.1 2.8-1.9 4zm2.3-6H9.7a14 14 0 0 1 0-4h4.6a14 14 0 0 1 0 4zm.3 5.9a15 15 0 0 0 1.3-3.9h3a8 8 0 0 1-4.3 3.9zm1.7-5.9a16 16 0 0 0 0-4h3.4a8 8 0 0 1 0 4z"/></svg>www.northfieldmw.com</li>
  </ul>
  <address class="address">120 Mill Creek Rd<br>Fairview, PA 17000</address>
  <div class="band">PRECISION MACHINING, COMPOSITES &amp; CLEAN ROOM MANUFACTURING</div>
</section>

</body>
</html>
```